Talvexa Official Investment Guide 2015

60 Second Animated Presentation to be showcased at a large Mining Convention. Presentation promotes the launch of KORVAL 2015, the Official Mining Investment Guide for the Convention. Also promotes TLW, the publisher. Presentation will be displayed in large screens on the exhibition floor, so it needs to be simple yet eye-catching and engaging. The cover of KORVAL is on definition phase, but it has been mostly completed - please follow those colors + the blue from TLW logo.
Reason: Organizer has extended the deadline to provide the video file.
Target Market(s)
Mining Professionals in Latin America
Industry/Entity Type
Mining
Requirements
Must have
- Animation as per Vidzora link included on the brief
- Strong Illustrations
Nice to have
- Music as per vidzora link included on the brief

```html
<!DOCTYPE html>
<html lang="es">
<head>
<meta charset="utf-8">
<title>¿Drones para estudiar la topografía de un proyecto minero?</title>
<link rel="stylesheet" href="https://fonts.googleapis.com/css2?family=Comfortaa:wght@300;700&display=swap">
<style>
  :root {
    --bg-deep: #0f3f8c;
    --bg-mid: #1d5aa6;
    --bg-light: #3a7fc1;
    --navy: #0c2766;
    --sky: #9cc3ec;
    --sky-soft: #b7d3f2;
    --white: #ffffff;
    --drone-tone: #dfe4ea;
  }
  * { margin: 0; padding: 0; box-sizing: border-box; }
  html, body { width: 1200px; height: 675px; overflow: hidden; }
  body { font-family: "Comfortaa", sans-serif; }
  .slide {
    position: relative;
    width: 1200px;
    height: 675px;
    overflow: hidden;
    background: linear-gradient(135deg, var(--bg-deep) 0%, var(--bg-mid) 55%, var(--bg-light) 100%);
  }
  .event-mark {
    position: absolute;
    left: 72px;
    top: 94px;
    color: var(--white);
    font-weight: 700;
    font-size: 15px;
    letter-spacing: 1.5px;
    line-height: 1;
  }
  .publisher-mark {
    position: absolute;
    right: 68px;
    top: 64px;
    color: var(--white);
    font-weight: 700;
    font-size: 24px;
    letter-spacing: 1px;
    line-height: 1;
  }
  .drone-art { position: absolute; left: 104px; top: 232px; }
  .headline { position: absolute; inset: 0; }
  .headline__line {
    position: absolute;
    white-space: nowrap;
    line-height: 1;
    transform: translate(-50%, -50%) rotate(-15deg);
  }
  .headline__line--drones { left: 712px; top: 206px; font-size: 106px; font-weight: 700; color: var(--navy); }
  .headline__line--study { left: 768px; top: 262px; font-size: 62px; font-weight: 300; color: var(--sky-soft); }
  .headline__line--topo { left: 812px; top: 318px; font-size: 66px; font-weight: 700; color: var(--sky); }
  .headline__line--project { left: 866px; top: 408px; font-size: 86px; font-weight: 700; color: var(--navy); }
  .headline__line--mining { left: 866px; top: 488px; font-size: 92px; font-weight: 700; color: var(--navy); }
  .headline__line--of {
    left: 630px; top: 494px; font-size: 52px; font-weight: 300; color: var(--sky-soft);
    transform: translate(-50%, -50%) rotate(75deg);
  }
</style>
</head>
<body>
  <main class="slide">
    <div class="event-mark">TALVEXA</div>
    <div class="publisher-mark">TLW</div>

    <svg class="drone-art" width="350" height="282" viewBox="0 0 350 282" role="img" aria-label="Ilustración de un dron cuadricóptero blanco con cámara">
      <rect x="0" y="0" width="350" height="282" rx="40" fill="var(--drone-tone)" opacity="0.22"/>
    </svg>

    <h1 class="headline">
      <span class="headline__line headline__line--drones">¿Drones</span>
      <span class="headline__line headline__line--study">para estudiar</span>
      <span class="headline__line headline__line--topo">la topografía</span>
      <span class="headline__line headline__line--of">de un</span>
      <span class="headline__line headline__line--project">proyecto</span>
      <span class="headline__line headline__line--mining">minero?</span>
    </h1>
  </main>
</body>
</html>
```